Buch-/E-Book-Cover für einen Thriller
Ich bin mehr als zufrieden mit dem Ergebnis und vor allem mit der Kommunikation! Super nett, kreativ und schnelle Anpassung und Übernahme von Vorschlägen. Die Zusammenarbeit hätte kaum besser laufen können und ich bin sicher, dass das auch nicht das letzte Mal gewesen ist. Mehr als empfehlenswert!

```html
<!DOCTYPE html>
<html lang="de">
<head>
<meta charset="utf-8">
<title>VIRUS – Thriller – Jan Becker</title>
<link rel="stylesheet" href="https://fonts.googleapis.com/css2?family=Oswald:wght@200;400;700&display=swap">
<style>
  :root {
    --bg-top: #0b0a0a;
    --bg-bottom: #060505;
    --red: #a2191f;
    --genre: #d6d6d6;
  }
  * { margin: 0; padding: 0; box-sizing: border-box; }
  html, body {
    width: 846px;
    height: 1200px;
    overflow: hidden;
    background: var(--bg-top);
  }
  .cover {
    position: relative;
    width: 846px;
    height: 1200px;
    background: var(--bg-top);
    overflow: hidden;
    font-family: "Oswald", sans-serif;
  }
  .cover__lower-band {
    position: absolute;
    left: 11px;
    right: 0;
    top: 789px;
    bottom: 0;
    background: var(--bg-bottom);
  }
  .cover__artwork {
    position: absolute;
    left: 146px;
    top: 128px;
    width: 560px;
    height: 570px;
  }
  .cover__title {
    position: absolute;
    left: 0;
    width: 846px;
    top: 726px;
    text-align: center;
    font-weight: 700;
    font-size: 184px;
    line-height: 1;
    letter-spacing: 16px;
    padding-left: 16px;
    color: var(--red);
  }
  .cover__genre {
    position: absolute;
    left: 0;
    width: 846px;
    top: 982px;
    text-align: center;
    font-weight: 200;
    font-size: 28px;
    line-height: 1.2;
    letter-spacing: 34px;
    padding-left: 34px;
    color: var(--genre);
  }
  .cover__author {
    position: absolute;
    left: 0;
    width: 846px;
    top: 1065px;
    text-align: center;
    font-weight: 400;
    font-size: 70px;
    line-height: 1.2;
    letter-spacing: 26px;
    padding-left: 26px;
    color: var(--red);
  }
</style>
</head>
<body>
  <main class="cover">
    <div class="cover__lower-band"></div>

    <svg class="cover__artwork" viewBox="0 0 560 570" role="img"
         aria-label="Illustration: großes rotes Symbol, von grauem Rauch umhüllt, auf schwarzem Grund">
      <defs>
        <radialGradient id="artwork-glow" cx="50%" cy="52%" r="50%">
          <stop offset="0%" stop-color="#3a1316"/>
          <stop offset="45%" stop-color="#6e1a1e"/>
          <stop offset="70%" stop-color="#3b1214"/>
          <stop offset="100%" stop-color="#0b0a0a" stop-opacity="0"/>
        </radialGradient>
      </defs>
      <ellipse cx="280" cy="290" rx="275" ry="280" fill="url(#artwork-glow)"/>
    </svg>

    <h1 class="cover__title">VIRUS</h1>
    <p class="cover__genre">THRILLER</p>
    <p class="cover__author">JAN BECKER</p>
  </main>
</body>
</html>
```